Varemo Group Business Card Design

The CEO is looking for a new trendy look for his business card.
You can stay with current branding or come up with something new/creative. It can be 3D, including Medical Office buildings. You can use our logo in a variety of colors. Please include name, title, company name, company website, email address, cell number

Target Market(s)

Real Estate Development and Construction

Industry/Entity Type

Health care real estate

Contact Information for Business Card

Rohesh Kumbar, CEO M-727.418.9062 E-roheshkumbar@varemo.com Address:4100 Lindell Ave, Tampa, FL 33611 www.varemo.com

Font styles to use
Other font styles liked:
• Be creative

Requirements
Must have
• Creative, trendy look
Nice to have
• Please go to our website to get a feel- www. varemo.com
Should not have
• small fonts

```html
<!DOCTYPE html>
<html lang="en">
<head>
<meta charset="utf-8">
<title>Varemo Group Business Card</title>
<link rel="stylesheet" href="https://fonts.googleapis.com/css2?family=Montserrat:wght@400;500;700;800&display=swap">
<style>
  :root {
    --bg: #e9e9ea;
    --card-white: #ffffff;
    --card-dark: #222223;
    --brand-red: #b01f2b;
    --ink: #1f1f1f;
    --ink-soft: #2b2b2b;
    --light: #ffffff;
  }
  * { box-sizing: border-box; margin: 0; padding: 0; }
  html, body {
    width: 1200px; height: 1200px; overflow: hidden;
    background: var(--bg);
    font-family: "Montserrat", Arial, sans-serif;
  }
  .canvas {
    width: 1200px; height: 1200px;
    display: flex; flex-direction: column; align-items: center; justify-content: center;
    gap: 60px;
  }
  .card {
    position: relative;
    width: 840px; height: 480px;
    border-radius: 40px;
    overflow: hidden;
    box-shadow: 0 10px 30px rgba(0,0,0,0.18);
  }
  .card--front { background: var(--card-white); }
  .card--back {
    background: var(--card-dark);
    border: 3px solid var(--brand-red);
    display: flex; align-items: center; justify-content: center;
  }

  .front-band { position: absolute; inset: 0; width: 100%; height: 100%; }
  .band-dark { fill: var(--card-dark); }
  .band-red { fill: var(--brand-red); }

  .wordmark {
    color: var(--brand-red);
    font-weight: 800;
    letter-spacing: -1px;
    line-height: 1;
  }
  .front-wordmark {
    position: absolute; right: 70px; top: 90px;
    font-size: 58px;
  }
  .back-wordmark { font-size: 96px; }

  .person { position: absolute; left: 80px; top: 180px; }
  .person-name {
    color: var(--brand-red);
    font-weight: 700;
    font-size: 40px;
    letter-spacing: 0.5px;
    line-height: 1.05;
  }
  .person-title {
    color: var(--ink);
    font-weight: 400;
    font-size: 30px;
    line-height: 1.1;
  }

  .contacts {
    position: absolute; left: 80px; top: 272px;
    list-style: none;
    display: flex; flex-direction: column; gap: 6px;
  }
  .contact-item {
    display: flex; align-items: center; gap: 14px;
    color: var(--ink-soft);
    font-size: 24px; font-weight: 500;
    line-height: 1.2;
  }
  .contact-icon { width: 26px; height: 26px; flex: none; }
  .contact-icon path, .contact-icon rect, .contact-icon circle { stroke: var(--brand-red); }

  .website {
    position: absolute; right: 44px; bottom: 48px;
    color: var(--light);
    font-size: 22px; font-weight: 500; letter-spacing: 1px;
    line-height: 1;
    white-space: nowrap;
  }
</style>
</head>
<body>
<main class="canvas">
  <section class="card card--front" aria-label="Business card front">
    <svg class="front-band" viewBox="0 0 840 480" preserveAspectRatio="none" aria-hidden="true">
      <path class="band-red" d="M0,430 L496,430 C546,430 552,352 602,352 L840,352 L840,366 L604,366 C558,366 552,444 500,444 L0,444 Z"/>
      <path class="band-dark" d="M0,448 L502,448 C554,448 560,370 606,370 L840,370 L840,480 L0,480 Z"/>
    </svg>

    <div class="wordmark front-wordmark">Varemo Group</div>

    <div class="person">
      <div class="person-name">ROHESH KUMBAR</div>
      <div class="person-title">CEO</div>
    </div>

    <ul class="contacts">
      <li class="contact-item">
        <svg class="contact-icon" viewBox="0 0 26 26" aria-hidden="true">
          <rect x="7" y="2" width="12" height="22" rx="2" fill="none" stroke-width="2.4"/>
          <path d="M11 20h4" stroke-width="2.4" stroke-linecap="round"/>
        </svg>
        <span>727.418.9062</span>
      </li>
      <li class="contact-item">
        <svg class="contact-icon" viewBox="0 0 26 26" aria-hidden="true">
          <rect x="2" y="6" width="22" height="15" fill="none" stroke-width="2.4"/>
          <path d="M2 6l11 9 11-9M2 21l8-7M24 21l-8-7" fill="none" stroke-width="2.4"/>
        </svg>
        <span>roheshkumbar@varemo.com</span>
      </li>
      <li class="contact-item">
        <svg class="contact-icon" viewBox="0 0 26 26" aria-hidden="true">
          <path d="M13 24s-8-8-8-13a8 8 0 0 1 16 0c0 5-8 13-8 13z" fill="none" stroke-width="2.4"/>
          <circle cx="13" cy="11" r="3" fill="none" stroke-width="2.4"/>
        </svg>
        <span>4100 Lindell Ave, Tampa, FL 33611</span>
      </li>
    </ul>

    <div class="website">www.varemo.com</div>
  </section>

  <section class="card card--back" aria-label="Business card back">
    <div class="wordmark back-wordmark">Varemo Group</div>
  </section>
</main>
</body>
</html>
```